Business Card Design

our business is purchasing, rehabbing and flipping homes. Design a house in the palm of a hand. This card is for a new company based in Georgia. So we buy homes that have been foreclosed, short sales,abandond, old homes and vacant homes.
We help improve the communities that we work in. We would like to see designs that use a black background with green accent and other colors that blend and don't take away from the logo and other important information.

Industry/Entity Type

Business

Contact Information for Business Card

Mavenbrook Holdings
Turning Old Doors Into New Starts
2738 Fenwick Lane
Duluth GA 30418
Office: 678-555-0192
mavenbrookholdingsllc.example

```html
<!DOCTYPE html>
<html lang="en">
<head>
<meta charset="utf-8">
<title>Mavenbrook Holdings – Business Card</title>
<link rel="stylesheet" href="https://fonts.googleapis.com/css2?family=Open+Sans:wght@400;600;700&family=Questrial&family=Libre+Baskerville&display=swap">
<style>
  :root {
    --bg: #d9d9d9;
    --black: #000000;
    --green: #429944;
    --white: #ffffff;
    --grey: #8c8c8c;
  }
  * { box-sizing: border-box; margin: 0; padding: 0; }
  html, body { width: 1200px; height: 900px; overflow: hidden; }
  body {
    background: var(--bg);
    font-family: "Open Sans", sans-serif;
    color: var(--white);
    position: relative;
  }
  .card {
    position: absolute;
    left: 270px;
    width: 660px;
    height: 377px;
    overflow: hidden;
    background: var(--green);
    box-shadow: 0 4px 14px rgba(0,0,0,.18);
  }
  .card--front { top: 50px; }
  .card--back { top: 473px; }

  .band { position: absolute; left: 0; width: 100%; background: var(--black); }
  .card--front .band--main { top: 75px; height: 257px; }

  .brand {
    position: absolute;
    display: flex;
    flex-direction: column;
    align-items: center;
    text-align: center;
  }
  .brand__mark {
    width: 58px; height: 58px;
    border-radius: 50%;
    background: var(--green);
    margin-bottom: 12px;
  }
  .brand__name {
    font-family: "Questrial", sans-serif;
    font-size: 24px;
    letter-spacing: .5px;
    color: var(--white);
    white-space: nowrap;
    line-height: 1;
  }
  .brand__tagline {
    font-family: "Libre Baskerville", serif;
    font-size: 9.5px;
    letter-spacing: .6px;
    color: var(--grey);
    text-transform: uppercase;
    margin-top: 4px;
    white-space: nowrap;
  }
  .card--front .brand { left: 0; right: 0; top: 128px; }

  .card--back .band--top { top: 0; height: 125px; }
  .card--back .band--logo { top: 0; left: 385px; width: 275px; height: 232px; }
  .card--back .band--foot { top: 345px; height: 32px; }
  .card--back .brand { left: 385px; width: 275px; top: 66px; }
  .card--back .brand__mark { width: 50px; height: 50px; margin-bottom: 10px; }
  .card--back .brand__name { font-size: 18px; }
  .card--back .brand__tagline { font-size: 7.5px; }

  .person { position: absolute; left: 38px; top: 138px; }
  .person__name { font-size: 25px; font-weight: 700; line-height: 1.15; }
  .person__title { font-size: 15px; font-weight: 400; }

  .contact {
    position: absolute;
    right: 24px;
    top: 240px;
    list-style: none;
    text-align: right;
  }
  .contact__item {
    display: flex;
    justify-content: flex-end;
    align-items: center;
    gap: 10px;
    font-size: 15.5px;
    line-height: 19.5px;
    white-space: nowrap;
  }
  .contact__icon { width: 12px; height: 12px; fill: var(--white); flex: none; }
</style>
</head>
<body>

<section class="card card--front" aria-label="Card front">
  <div class="band band--main"></div>
  <div class="brand">
    <span class="brand__mark"></span>
    <span class="brand__name">MAVENBROOK HOLDINGS</span>
    <span class="brand__tagline">Turning Old Doors Into New Starts</span>
  </div>
</section>

<section class="card card--back" aria-label="Card back">
  <div class="band band--top"></div>
  <div class="band band--logo"></div>
  <div class="band band--foot"></div>

  <div class="brand">
    <span class="brand__mark"></span>
    <span class="brand__name">MAVENBROOK HOLDINGS</span>
    <span class="brand__tagline">Turning Old Doors Into New Starts</span>
  </div>

  <div class="person">
    <p class="person__name">Daniel Harper</p>
    <p class="person__title">Managing Director</p>
  </div>

  <ul class="contact">
    <li class="contact__item">678-555-0192
      <svg class="contact__icon" viewBox="0 0 12 12"><path d="M1 4c0-2 2-3 5-3s5 1 5 3l-2 1-1-2H4L3 5zM3 6h6l1 5H2z"/></svg>
    </li>
    <li class="contact__item">678-555-0192
      <svg class="contact__icon" viewBox="0 0 12 12"><path d="M3 1h6v3H3zM1 5h10v5H9V8H3v2H1zM4 9h4v2H4z"/></svg>
    </li>
    <li class="contact__item">hello@mavenbrook.example
      <svg class="contact__icon" viewBox="0 0 12 12"><path d="M0 2h12v1L6 7 0 3zM0 4.5l6 4 6-4V10H0z"/></svg>
    </li>
    <li class="contact__item">mavenbrookholdingsllc.example
      <svg class="contact__icon" viewBox="0 0 12 12"><path d="M5 7l2-2 .8.8-2 2zM3 6l-2 2a2 2 0 003 3l2-2-1-1-2 2a.7.7 0 01-1-1l2-2zM9 6l2-2a2 2 0 00-3-3L6 3l1 1 2-2a.7.7 0 011 1L8 5z"/></svg>
    </li>
    <li class="contact__item">2738 Fenwick Lane, Duluth GA 30418
      <svg class="contact__icon" viewBox="0 0 12 12"><path d="M6 0a4 4 0 00-4 4c0 3 4 8 4 8s4-5 4-8a4 4 0 00-4-4zm0 2.5A1.5 1.5 0 116 5.5 1.5 1.5 0 016 2.5z"/></svg>
    </li>
  </ul>
</section>

</body>
</html>
```